Website Design for my Copper Distillation Equipment Business Nature Sciencey Theme

I already have a website www.halvorkettleworks.com and its a pixelhut website builder one. But I cannot get the design right at all. I need this fixed.

I have logo. I need a redesign, for my website, the home page, that maybe I can have something similar in design- I can use as template to copy, for other pages so the whole thing matches? Look at my website so you understand I have a few pages...but most are links. Its a competition. Code has to be easy for me to implement, I am not expert.

Your advice needed..It would be a plus if I can update this myself throughout time. If I could have this explained to me too, the maintenance of it...how would I do this too..etc..pretend I am a child when you explain, if you can. I am not good with this stuff but I am smart and can learn fast.

I want a high end look. Maybe like an ivy league college-y look too, real preppy, chemistry...science-y, nature like is good, leaves, drops water, fields of wheat, lavender, etc.

I want every page to look similar, but the home page is what I want to be the main showpiece,..and I want each page have a little text section, maybe a photos section and a video section, for that market. Like a nice website. If I am not doing this right, let me know. I can work with you. Just help me, please. Let me know if I am doing this right.

When I pick my winning design, for my website, I will hire the artist one-on-one to re-design my shopping cart next. Or if I need additional help with implementing this current design, I can hire the same artist again too. I have a blog that I may want to hire the redesign as well too, but later on. My point is I am not just looking for one project here but I want to follow up with winning artist. So it would be return business for the winner.

I got my logo done here so I am repeat customer. And I have given that winning artist other design work.

Target Market(s)

Moonshine Stills I sell most, Essential Oil Business, Micro and Craft Distilleries, Canna-businesses, Alcohol Fuel

Industry/Entity Type

Business

Number of Pages Required

5+ page

Colors
ec1f27

Requirements
Must have
• The categories for the stills must be prominent and eye catching. The main photo I would like to be naturelike theme, but you can try out different things with me. I am open to ideas and suggestions. I would like this to be implemented easy and fast.
Nice to have
• My logo in it. You can use any of my photos as well from my snapvale account. https://www.snapvale.net/photos/81726354@X07/
• Colors of my Logo...matching design.
• Maybe some basic stock photos you see would match for me..
• Chemistry like symbols for the categories, I love that.

```html
<!DOCTYPE html>
<html lang="en">
<head>
<meta charset="utf-8">
<title>Halvor Kettleworks – Copper Distillation Equipment</title>
<link href="https://fonts.googleapis.com/css2?family=Lato:wght@400;700;900&display=swap" rel="stylesheet">
<style>
:root{
  --red:#ec1f27;
  --red-dark:#6b1013;
  --ink:#333333;
  --muted:#666666;
  --light:#f0f0f0;
  --nav:#ececec;
  --line:#dddddd;
  --dark:#1d1d1d;
  --darker:#141414;
  --white:#ffffff;
  --footer-text:#9a9a9a;
}
*{box-sizing:border-box;margin:0;padding:0}
html,body{width:1200px;height:2762px;overflow:hidden}
body{font-family:'Lato',sans-serif;color:var(--ink);background:var(--white);position:relative}
a{color:inherit;text-decoration:none}
.abs{position:absolute}
.hex{clip-path:polygon(50% 0,100% 25%,100% 75%,50% 100%,0 75%,0 25%)}
.btn{position:absolute;background:var(--red);color:var(--white);font-size:11px;font-weight:700;border-radius:14px;display:flex;align-items:center;justify-content:center;gap:6px;letter-spacing:.3px;white-space:nowrap}
.btn .dot{width:11px;height:11px;border-radius:50%;background:var(--white);display:inline-flex;align-items:center;justify-content:center}
.btn .dot::after{content:"";border-left:4px solid var(--red);border-top:3px solid transparent;border-bottom:3px solid transparent;margin-left:1px}
.section-title{position:absolute;color:var(--red);font-size:24px;font-weight:400;display:flex;align-items:center;gap:6px;white-space:nowrap}
.section-title .tick{display:inline-flex;align-items:center}
.section-title .tick::before{content:"";width:8px;height:8px;border-radius:50%;background:var(--red)}
.section-title .tick::after{content:"";width:22px;height:1px;background:var(--red)}
.section-title .tick.left{flex-direction:row-reverse}
.body-text{font-size:11px;line-height:18px;color:var(--muted)}

/* social links */
.social{position:absolute;display:flex;gap:10px}
.social a{width:32px;height:36px;background:var(--red);color:var(--white);font-size:8px;font-weight:700;display:flex;align-items:center;justify-content:center;letter-spacing:.2px}
.social.small{gap:8px}
.social.small a{width:30px;height:34px;font-size:7.5px}
.social.small a.dim{background:var(--red-dark)}

/* header */
.site-header{position:absolute;left:0;top:0;width:1200px;height:111px}
.contact-item{position:absolute;top:38px;display:flex;align-items:center;gap:12px;font-size:12px;color:var(--red);white-space:nowrap}
.contact-item .hex{width:32px;height:36px;background:var(--red);display:flex;align-items:center;justify-content:center}
.brand{position:absolute;left:520px;top:22px;width:160px;height:70px;display:flex;flex-direction:column;align-items:center;justify-content:center;gap:2px}
.brand .mark{font-size:30px;font-weight:900;color:var(--dark);letter-spacing:1px;line-height:1}
.brand .name{font-size:8px;font-weight:700;color:var(--dark);letter-spacing:2px;text-transform:uppercase;white-space:nowrap}

/* nav */
.main-nav{position:absolute;top:111px;left:0;width:1200px;height:43px;background:var(--nav)}
.main-nav a{position:absolute;top:11px;font-size:11px;color:var(--ink);transform:translateX(-50%);padding:4px 14px;white-space:nowrap}
.main-nav a.active{color:var(--red);border:1px solid var(--red)}

/* hero */
.hero{position:absolute;top:154px;left:0;width:1200px;height:507px;background:linear-gradient(100deg,#6e6a66 0%,#a7a39c 22%,#c9c6c0 45%,#5b5d63 70%,#3b3e44 100%)}
.hero-arrow{position:absolute;top:388px;width:38px;height:42px;background:var(--red);display:flex;align-items:center;justify-content:center}

/* welcome */
.welcome-photo{position:absolute;left:186px;top:713px;width:191px;height:220px;background:linear-gradient(160deg,#8b5a2e,#c48a4f 50%,#5d6f8c)}
.welcome-text{position:absolute;left:398px;top:752px;width:620px;font-size:10px;line-height:15px;color:var(--ink)}
.welcome-text p+p{margin-top:15px}

/* categories */
.categories{position:absolute;top:985px;left:0;width:1200px;height:433px;background:var(--light)}
.cat-list{position:absolute;left:186px;top:1040px;width:189px;height:328px;background:var(--white);border:1px solid var(--line);padding:20px 13px 0 13px;list-style:none}
.cat-list li{font-size:10px;color:var(--ink);height:27px;display:flex;align-items:center;gap:10px;border-bottom:1px solid var(--line)}
.cat-list li:last-child{border-bottom:none}
.cat-list li::before{content:"";width:10px;height:10px;border-radius:50%;background:var(--red);flex:none}
.card{position:absolute;top:1040px;width:190px;height:328px;background:var(--white);border:1px solid var(--line)}
.card .photo{position:absolute;left:8px;top:9px;width:174px;height:161px}
.card h3{position:absolute;left:8px;top:182px;width:174px;text-align:center;font-size:11.5px;line-height:15px;font-weight:700;color:var(--red);text-transform:uppercase}
.card p{position:absolute;left:8px;top:228px;width:174px;font-size:10px;line-height:14px;color:var(--muted);text-align:justify}

/* how it works */
.how-text{position:absolute;left:184px;top:1512px;width:336px}
.video{position:absolute;left:541px;top:1472px;width:475px;height:269px;background:linear-gradient(135deg,#8d8f90,#c2c1bb 45%,#6b4a3c)}
.video .bar{position:absolute;left:0;bottom:0;width:100%;height:22px;background:rgba(0,0,0,.75)}
.video .top{position:absolute;left:0;top:0;width:100%;height:22px;background:rgba(0,0,0,.8)}
.video .play{position:absolute;left:212px;top:108px;width:52px;height:40px;border-radius:50%;background:var(--red);display:flex;align-items:center;justify-content:center}

/* gallery */
.gallery{position:absolute;top:1793px;left:0;width:1200px;height:375px;background:var(--light)}
.gallery .hex{position:absolute;top:104px;width:191px;height:219px}

/* news & testimonials */
.news-item{position:absolute;left:184px;width:420px;height:60px}
.news-item .date{position:absolute;left:0;top:0;width:50px;height:57px;background:var(--red);color:var(--white);display:flex;flex-direction:column;align-items:center;justify-content:center;line-height:1}
.news-item .date b{font-size:18px;font-weight:400}
.news-item .date span{font-size:8px;text-transform:uppercase;margin-top:2px}
.news-item h4{position:absolute;left:70px;top:-2px;font-size:17px;font-weight:700;color:var(--dark);white-space:nowrap}
.news-item p{position:absolute;left:70px;top:22px;width:340px;font-size:10px;line-height:14px;color:var(--muted)}
.testimonial-photo{position:absolute;left:768px;top:2270px;width:92px;height:104px;background:var(--red);display:flex;align-items:center;justify-content:center}
.testimonial-photo .inner{width:86px;height:98px;background:linear-gradient(180deg,#e8e8e8,#9b9fa6)}
.dots{position:absolute;left:792px;top:2474px;display:flex;gap:6px}
.dots i{width:9px;height:9px;border-radius:50%;background:var(--red)}
.dots i.off{background:var(--white);border:2px solid var(--red)}

/* footer */
.site-footer{position:absolute;top:2536px;left:0;width:1200px;height:173px;background:var(--dark)}
.footer-contact{position:absolute;left:184px;top:78px;font-size:12px;color:var(--white);white-space:nowrap}
.footer-brand{position:absolute;left:530px;top:50px;width:140px;height:76px;display:flex;flex-direction:column;align-items:center;justify-content:center;gap:3px;color:var(--white)}
.footer-brand .mark{font-size:28px;font-weight:900;line-height:1}
.footer-brand .name{font-size:7px;font-weight:700;letter-spacing:2px;white-space:nowrap}
.footer-bottom{position:absolute;top:2709px;left:0;width:1200px;height:53px;background:var(--darker);font-size:9px;color:var(--footer-text)}
.footer-bottom nav a{position:absolute;top:22px;color:var(--footer-text)}
.footer-bottom .copyright{position:absolute;right:184px;top:22px;white-space:nowrap}
</style>
</head>
<body>

<header class="site-header">
  <div class="contact-item" style="left:183px">
    <span class="hex"><svg width="14" height="14" viewBox="0 0 24 24"><path fill="#fff" d="M6.6 10.8a15.1 15.1 0 0 0 6.6 6.6l2.2-2.2c.3-.3.7-.4 1-.2 1.1.4 2.3.6 3.6.6.6 0 1 .4 1 1V20c0 .6-.4 1-1 1A17 17 0 0 1 3 4c0-.6.4-1 1-1h3.5c.6 0 1 .4 1 1 0 1.3.2 2.5.6 3.6.1.3 0 .7-.2 1z"/></svg></span>
    <span>360-555-0148</span>
  </div>
  <div class="contact-item" style="left:308px">
    <span class="hex"><svg width="14" height="12" viewBox="0 0 24 18"><rect x="1" y="1" width="22" height="16" fill="none" stroke="#fff" stroke-width="2"/><path d="M1 1l11 9 11-9" fill="none" stroke="#fff" stroke-width="2"/></svg></span>
    <span>ingrid@halvorkettleworks.com</span>
  </div>
  <div class="brand"><span class="mark">HK</span><span class="name">Halvor Kettleworks</span></div>
  <nav class="social" style="left:856px;top:37px" aria-label="Social links">
    <a class="hex">Loop</a><a class="hex">Chirp</a><a class="hex">Wire</a><a class="hex">Orb</a>
  </nav>
</header>

<nav class="main-nav">
  <a class="active" style="left:217px">Home</a>
  <a style="left:318px">About Us</a>
  <a style="left:429px">Contact Us</a>
  <a style="left:533px">Photo</a>
  <a style="left:626px">Video</a>
  <a style="left:715px">Shop</a>
  <a style="left:803px">Blog</a>
  <a style="left:892px">Books</a>
  <a style="left:983px">Links</a>
</nav>

<section class="hero" role="img" aria-label="Close-up photo of a glass and copper distillation column in a workshop"></section>
<span class="hero-arrow hex" style="left:22px"><svg width="10" height="12" viewBox="0 0 10 12"><path d="M8 1L3 6l5 5" fill="none" stroke="#fff" stroke-width="2"/></svg></span>
<span class="hero-arrow hex" style="left:1140px"><svg width="10" height="12" viewBox="0 0 10 12"><path d="M2 1l5 5-5 5" fill="none" stroke="#fff" stroke-width="2"/></svg></span>

<section class="welcome">
  <div class="welcome-photo hex" role="img" aria-label="Photo of the owner working at a copper still in a kitchen"></div>
  <h2 class="section-title" style="left:398px;top:708px">Welcome To Our Website.<span class="tick left"></span></h2>
  <div class="welcome-text">
    <p>Are you looking for a Moonshine Still? Are you a Lavender Farm? Are you wanting to distill Essential Oils on your farm and make Hydrosols too? Do you want to make an Herbal Extraction or Tincture? Do you want to start a Home Business? Are you a Micro (small) Distillery wanting a Set up? Are you a Race Car driver looking for alternative ways to get your Ethanol? Are you a Prepper? Are you interested in Making Alcohol in times of Survival? Do you need clean radiation free Water for your community? Do you want to support Local Farmers, get back to the Source and Nature? Are you a Canna business or 502?</p>
    <p>My Dream Costomer is someone who believes they cannot, but does it anyways and finds out they can! And then they go and teach someone....that is a gift that keeps on giving. Those are the results I want to give. Taking a liquid, turning it into a vapor and then back into a liquid. That is all you need to know.</p>
  </div>
  <span class="btn" style="left:398px;top:907px;width:112px;height:26px">LEARN MORE <span class="dot"></span></span>
</section>

<section class="categories"></section>
<ul class="cat-list">
  <li>Stills</li><li>Essential Oils</li><li>Alcohol Fuel</li><li>Cannabis</li><li>Boilers</li><li>Home Distillers</li><li>Vodka Still</li><li>Heat Control</li><li>Distillery</li><li>Kits</li><li>Parts</li>
</ul>
<article class="card" style="left:398px">
  <div class="photo" role="img" aria-label="Photo of copper pot stills outdoors among trees" style="background:linear-gradient(180deg,#3f6b2e,#8aa36c 45%,#b9b4a8)"></div>
  <h3>Home Distillers! We sell copper stills.</h3>
  <p>Lorem ipsum dolor sit amet, consectetuer adipiscing elit, sed diam nonummy nibh euismod tincidunt ut</p>
  <span class="btn" style="left:46px;top:284px;width:98px;height:26px">READ MORE <span class="dot"></span></span>
</article>
<article class="card" style="left:611px">
  <div class="photo" role="img" aria-label="Photo of micro distillery copper still with control panel" style="background:linear-gradient(180deg,#4d6d3a,#9ea6a8 50%,#6f7f93)"></div>
  <h3>Micro Distillery Equipm-ent copper still for sale</h3>
  <p>Lorem ipsum dolor sit amet, consectetuer adipiscing elit, sed diam nonummy nibh euismod tincidunt ut</p>
  <span class="btn" style="left:46px;top:284px;width:98px;height:26px">READ MORE <span class="dot"></span></span>
</article>
<article class="card" style="left:825px">
  <div class="photo" role="img" aria-label="Photo of herbal extraction equipment on a chalkboard table" style="background:linear-gradient(160deg,#3d4f4a,#6f7f78 45%,#2f55a0)"></div>
  <h3>Witch herbal extractor makecannabis oil with</h3>
  <p>Lorem ipsum dolor sit amet, consectetuer adipiscing elit, sed diam nonummy nibh euismod tincidunt ut</p>
  <span class="btn" style="left:46px;top:284px;width:98px;height:26px">READ MORE <span class="dot"></span></span>
</article>

<section class="how">
  <h2 class="section-title" style="left:183px;top:1466px">How It Works<span class="tick left"></span></h2>
  <div class="how-text body-text">
    <p>Lorem ipsum dolor sit amet, consectetuer adipiscing elit, sed diam nonummy nibh euismod tincidunt ut laoreet dolore magna aliquam erat volutpat. Ut wisi enim ad minim veniam, quis nostrud exerci tation ullamcorper suscipit lobortis nisl ut aliquip ex ea commodo consequat.</p>
    <p style="margin-top:18px">Duis autem vel eum iriure dolor in hendrerit in vulputate velit esse molestie consequat, vel illum dolore eu feugiat nulla facilisis at vero eros et accumsan et iusto odio dignissim qui blandit praesent luptatum zzril delenit augue.</p>
  </div>
  <span class="btn" style="left:184px;top:1707px;width:99px;height:33px;border-radius:3px">READ MORE</span>
  <div class="video" role="img" aria-label="Video still of two men standing beside distillation equipment">
    <span class="top"></span>
    <span class="play"><svg width="16" height="18" viewBox="0 0 16 18"><path d="M2 1l13 8-13 8z" fill="#fff"/></svg></span>
    <span class="bar"></span>
  </div>
</section>

<section class="gallery">
  <h2 class="section-title" style="left:524px;top:44px"><span class="tick"></span>Gallery<span class="tick left"></span></h2>
  <div class="hex" style="left:186px;background:linear-gradient(160deg,#6f6a3a,#c9c6a0 55%,#4b4a3f)" role="img" aria-label="Photo of a man holding a glass of distillate"></div>
  <div class="hex" style="left:398px;background:linear-gradient(170deg,#d9dde0,#c9b24a 60%,#5c7a3a)" role="img" aria-label="Photo of a jar with golden essential oil"></div>
  <div class="hex" style="left:611px;background:linear-gradient(160deg,#f2f2f2,#b68a5e 55%,#6e8a4f)" role="img" aria-label="Photo of a man beside a copper still"></div>
  <div class="hex" style="left:823px;background:linear-gradient(170deg,#6a8c4a,#3f5fa8 50%,#b7a27d)" role="img" aria-label="Photo of a woman operating a still outdoors"></div>
</section>

<section class="news">
  <h2 class="section-title" style="left:183px;top:2216px">Letest News<span class="tick left"></span></h2>
  <article class="news-item" style="top:2297px">
    <div class="date hex"><b>06</b><span>May</span></div>
    <h4>Lorem ipsum dolor sit amet, consectetuer</h4>
    <p>sed diam nonummy nibh euismod tincidunt ut laoreet dolore magna aliquam erat volutpat. Ut wisi enim ad minim veniam,</p>
  </article>
  <article class="news-item" style="top:2374px">
    <div class="date hex"><b>15</b><span>Jan</span></div>
    <h4>Lorem ipsum dolor sit amet, consectetuer</h4>
    <p>sed diam nonummy nibh euismod tincidunt ut laoreet dolore magna aliquam erat volutpat. Ut wisi enim ad minim veniam,</p>
  </article>
  <article class="news-item" style="top:2451px">
    <div class="date hex"><b>26</b><span>Feb</span></div>
    <h4>Lorem ipsum dolor sit amet, consectetuer</h4>
    <p>sed diam nonummy nibh euismod tincidunt ut laoreet dolore magna aliquam erat volutpat. Ut wisi enim ad minim veniam,</p>
  </article>
</section>

<section class="testimonials">
  <h2 class="section-title" style="left:710px;top:2216px"><span class="tick"></span>Testimonials<span class="tick left"></span></h2>
  <div class="testimonial-photo hex"><div class="inner hex" role="img" aria-label="Portrait photo of a customer"></div></div>
  <div class="abs" style="left:614px;top:2380px;width:400px;text-align:center;font-size:16px;color:var(--red)">Maren Okafor</div>
  <svg class="abs" style="left:804px;top:2410px" width="16" height="12" viewBox="0 0 16 12"><path d="M0 12V6C0 2 2 0 6 0v2C4 2 3 3 3 5h3v7zM9 12V6c0-4 2-6 6-6v2c-2 0-3 1-3 3h3v7z" fill="#999"/></svg>
  <p class="abs" style="left:624px;top:2428px;width:380px;text-align:center;font-size:10px;line-height:15px;color:var(--ink)">Lorem ipsum dolor sit amet, consectetuer adipiscing elit, sed diam nonummy nibh euismod tincidunt ut laoreet dolore magna aliquam erat volutpat.</p>
  <div class="dots"><i></i><i class="off"></i><i></i></div>
</section>

<footer class="site-footer">
  <div class="footer-contact">ingrid@halvorkettleworks.com &nbsp;&nbsp;&nbsp;|&nbsp;&nbsp;&nbsp; 360-555-0148</div>
  <div class="footer-brand"><span class="mark">HK</span><span class="name">HALVOR KETTLEWORKS</span></div>
  <nav class="social small" style="left:822px;top:70px" aria-label="Social links">
    <a class="hex">Loop</a><a class="hex dim">Chirp</a><a class="hex dim">Wire</a><a class="hex dim">Orb</a><a class="hex dim">Tack</a>
  </nav>
</footer>
<div class="footer-bottom">
  <nav>
    <a style="left:184px">Home</a>
    <a style="left:243px">About Us</a>
    <a style="left:317px">Shop Now</a>
    <a style="left:394px">Gallery</a>
    <a style="left:459px">Book</a>
    <a style="left:514px">Contact Us</a>
  </nav>
  <div class="copyright">© 2015 halvorkettleworks.com &nbsp;|&nbsp; All Rights Reserved.</div>
</div>

</body>
</html>
```